Coaching and Tutoring that removes all obstacles and leads to success and happiness

Tutoring maths giving confidence, clarity and success to students of all abilities. Tutoring from 14 years to 18 years old. Dealing with exam preparation and stress.
Coaching confidence, resilience and ultimately happiness and freedom.
The design to inspire and reassure people of a safe pair of hands as well excitement of the beginning of something new in their lives.

Target Market(s)

20 -30 year olds

Industry/Entity Type

Self Development and Education

Contact Information for Business Card

Confidence Coach and Maths Tutor

Font styles to use
Sans Serif

Colors
EE7325
F08F49
F5BC92
FAE3D3
FDF4ED

Requirements
Must have
• Success and Happiness

```html
<!DOCTYPE html>
<html lang="en">
<head>
<meta charset="utf-8">
<title>Maren Holt Coaching – Business Card</title>
<link href="https://fonts.googleapis.com/css2?family=Cinzel:wght@500&family=Arimo:wght@400&family=Bebas+Neue&display=swap" rel="stylesheet">
<style>
  :root{
    --bg:#2b2b2d;
    --card:#0b0b0c;
    --green:#7ab632;
    --orange:#ee7325;
    --text:#e8e8e8;
    --divider:#3a3a3c;
    --photo-top:#5e6670;
    --photo-bottom:#252c20;
  }
  *{margin:0;padding:0;box-sizing:border-box}
  html,body{width:1200px;height:900px;overflow:hidden;background:var(--bg)}
  .canvas{width:1200px;height:900px;display:flex;align-items:center;justify-content:center;gap:40px}
  .card{width:540px;height:310px;border-radius:22px;overflow:hidden;position:relative;background:var(--card);box-shadow:0 18px 40px rgba(0,0,0,.5)}
  /* front */
  .card-front{display:flex}
  .brand{width:52%;display:flex;flex-direction:column;align-items:center;justify-content:center;gap:18px}
  .brand-dot{width:54px;height:54px;border-radius:50%;background:var(--green)}
  .brand-name{font-family:"Cinzel",serif;font-weight:500;color:var(--green);font-size:27px;letter-spacing:1px;text-align:center;line-height:1.25}
  .divider{width:1px;background:var(--divider);margin:40px 0}
  .contact{flex:1;display:flex;flex-direction:column;justify-content:center;padding-left:26px}
  .contact-name{font-family:"Cinzel",serif;font-weight:500;color:var(--green);font-size:20px;letter-spacing:1px;margin-bottom:14px}
  .contact-list{list-style:none;font-family:"Arimo",sans-serif;font-size:13.5px;color:var(--text)}
  .contact-list li{display:flex;align-items:center;gap:10px;margin-bottom:7px}
  .contact-list svg{width:15px;height:15px;flex:none}
  .accent{color:var(--green)}
  /* back */
  .card-back .photo{position:absolute;inset:0;background:linear-gradient(160deg, var(--photo-top) 0%, var(--photo-bottom) 100%)}
  .tagline{position:absolute;right:28px;bottom:26px;font-family:"Bebas Neue",sans-serif;color:var(--green);font-size:40px;letter-spacing:.5px}
</style>
</head>
<body>
<main class="canvas">
  <section class="card card-front">
    <div class="brand">
      <span class="brand-dot"></span>
      <p class="brand-name">Maren Holt<br>Coaching</p>
    </div>
    <div class="divider"></div>
    <div class="contact">
      <h1 class="contact-name">Maren Holt</h1>
      <ul class="contact-list">
        <li>
          <svg viewBox="0 0 24 24"><path fill="var(--orange)" d="M6.6 10.8a15.1 15.1 0 0 0 6.6 6.6l2.2-2.2c.3-.3.7-.4 1-.2 1.1.4 2.3.6 3.6.6.6 0 1 .4 1 1V20c0 .6-.4 1-1 1A17 17 0 0 1 3 4c0-.6.4-1 1-1h3.5c.6 0 1 .4 1 1 0 1.3.2 2.5.6 3.6.1.3 0 .7-.2 1z"/></svg>
          +44 (0) 7700 900418
        </li>
        <li>
          <svg viewBox="0 0 24 24"><rect x="2" y="5" width="20" height="14" fill="var(--orange)"/><path d="M2 5l10 8 10-8" fill="none" stroke="var(--card)" stroke-width="1.6"/></svg>
          marenholt@mailbox.com
        </li>
        <li>
          <svg viewBox="0 0 24 24"><g fill="none" stroke="var(--orange)" stroke-width="2"><circle cx="12" cy="12" r="9"/><ellipse cx="12" cy="12" rx="4" ry="9"/><path d="M3 12h18M5 7h14M5 17h14"/></g></svg>
          <span>www.<span class="accent">marenholt</span>.com</span>
        </li>
      </ul>
    </div>
  </section>

  <section class="card card-back">
    <div class="photo" role="img" aria-label="Photograph of a person at a wooden gate on a country path, backlit by a low sun with bare trees"></div>
    <p class="tagline">Success and Happiness</p>
  </section>
</main>
</body>
</html>
```